RTB Weissbier: Art NOUVEAU Illustration & Beer Label

We want your help for a really exquisite project.
We are to launch a traditional weissbier with very noble Mitteleuropa pedigree.

Name: RTB
...from Reinhold Tobias Baumgart, the last Austro-Hungarian emperor.
https://en.quellarchiv.example/wiki/Reinhold_Tobias_Baumgart

We want to play on the letters RTB (with their dual meaning) and the iconic figure of the emperor. Illustration skills are absolutely critical. We want this to look like 1900-1914 avant-garde. See attached references for the emperor figure and some feel references for the epoque.

This beer is a traditional Weissbier born in Lindgrube, in a craft Bavarian brewery that dates from 1853.

Target Market(s)

Europe

Colors

Designer to choose colors to be used in the design.

Requirements
Must have
• Illustration of the Emperor in great art deco style
• Should look more like a painting / poster than a computer made vectorial
• Practicalities as per attached file
Nice to have
• The emperor appreciating a glass of his Weissbier
• RTB the beer name written with great Art Deco fonts, looking like it was handcrafted
• Faded blue tones & yolk yellow.

```html
<!DOCTYPE html>
<html lang="en">
<head>
<meta charset="utf-8">
<title>RTB Weissbier – Label</title>
<link rel="stylesheet" href="https://fonts.googleapis.com/css2?family=Anton&family=Josefin+Sans:wght@700&family=Oswald:wght@400;500;600&display=swap">
<style>
  :root {
    --page: #ffffff;
    --yolk-light: #f5d77a;
    --yolk: #eec55a;
    --yolk-deep: #dcaa3c;
    --ink: #1e1a12;
    --ribbon: #f7e6ab;
    --ribbon-pill: #e8c46a;
    --ribbon-text: #6a5836;
    --portrait-blue: #7fb0d6;
    --portrait-skin: #e9c9a4;
    --hop-tone: #c9a545;
  }
  html, body {
    margin: 0;
    padding: 0;
    width: 1200px;
    height: 1200px;
    overflow: hidden;
    background: var(--page);
  }
  .canvas {
    position: relative;
    width: 1200px;
    height: 1200px;
    overflow: hidden;
    background: var(--page);
  }
  .label {
    position: absolute;
    left: 82px;
    top: 50px;
    width: 1037px;
    height: 1100px;
    box-shadow: 0 2px 10px rgba(0,0,0,0.08);
  }
  .story { font-family: "Oswald", sans-serif; font-weight: 500; font-size: 19px; fill: var(--ink); }
  .ring-title { font-family: "Josefin Sans", sans-serif; font-weight: 700; font-size: 24px; letter-spacing: 6px; fill: var(--ink); }
  .brand-mark { font-family: "Anton", sans-serif; font-size: 64px; letter-spacing: 26px; fill: var(--ink); }
  .origin { font-family: "Oswald", sans-serif; font-weight: 500; font-size: 14px; letter-spacing: 4px; fill: var(--ribbon-text); }
  .full-name { font-family: "Oswald", sans-serif; font-weight: 600; font-size: 29px; letter-spacing: 1px; fill: var(--ink); }
  .specs { font-family: "Oswald", sans-serif; font-weight: 500; font-size: 12px; fill: var(--ink); }
  .volume { font-family: "Oswald", sans-serif; font-weight: 600; font-size: 30px; fill: var(--ink); }
  .rule { stroke: var(--ink); fill: none; }
  .rays line { stroke: var(--ink); stroke-width: 1.2; }
</style>
</head>
<body>
<div class="canvas">
  <svg class="label" viewBox="0 0 608 645" xmlns="http://www.w3.org/2000/svg">
    <defs>
      <linearGradient id="paper" x1="0" y1="0" x2="1" y2="1">
        <stop offset="0" stop-color="var(--yolk-light)"/>
        <stop offset="0.55" stop-color="var(--yolk)"/>
        <stop offset="1" stop-color="var(--yolk-deep)"/>
      </linearGradient>
      <radialGradient id="medallion" cx="0.5" cy="0.4" r="0.6">
        <stop offset="0" stop-color="#fbe8a8"/>
        <stop offset="1" stop-color="#f0cd6a"/>
      </radialGradient>
      <linearGradient id="portrait-tone" x1="0" y1="0" x2="0" y2="1">
        <stop offset="0" stop-color="var(--portrait-skin)"/>
        <stop offset="0.5" stop-color="#d9c3a6"/>
        <stop offset="1" stop-color="var(--portrait-blue)"/>
      </linearGradient>
      <clipPath id="medallion-clip">
        <circle cx="304" cy="313" r="152"/>
      </clipPath>
      <clipPath id="frame-clip">
        <rect x="24" y="24" width="560" height="597"/>
      </clipPath>
      <path id="ring-arc" d="M157,245 A162 162 0 0 1 451,245"/>
    </defs>

    <!-- paper -->
    <rect class="paper" x="0" y="0" width="608" height="645" fill="url(#paper)"/>

    <!-- frames -->
    <rect class="rule" x="8" y="8" width="592" height="629" stroke-width="2"/>
    <rect class="rule" x="14" y="14" width="580" height="617" stroke-width="1" stroke-dasharray="2 3"/>
    <path class="rule" stroke-width="2" d="M40,24 H568 A16 16 0 0 0 584 40 V605 A16 16 0 0 0 568 621 H40 A16 16 0 0 0 24 605 V40 A16 16 0 0 0 40 24 Z"/>

    <!-- story -->
    <text class="story" x="304" y="66" text-anchor="middle">BORN IN LINDGRUBE, BAVARIA, IN A CRAFT BREWERY</text>
    <text class="story" x="304" y="100" text-anchor="middle">THAT WAS ESTABLISHED IN 1853.</text>

    <!-- rays -->
    <g class="rays" clip-path="url(#frame-clip)">
      <line x1="104" y1="313" x2="40" y2="313"/>
      <line x1="107" y1="278" x2="38" y2="266"/>
      <line x1="116" y1="245" x2="50" y2="221"/>
      <line x1="107" y1="348" x2="38" y2="360"/>
      <line x1="116" y1="381" x2="50" y2="405"/>
      <line x1="504" y1="313" x2="568" y2="313"/>
      <line x1="501" y1="278" x2="570" y2="266"/>
      <line x1="492" y1="245" x2="558" y2="221"/>
      <line x1="501" y1="348" x2="570" y2="360"/>
      <line x1="492" y1="381" x2="558" y2="405"/>
      <line x1="250" y1="120" x2="238" y2="108"/>
      <line x1="358" y1="120" x2="370" y2="108"/>
    </g>

    <!-- hop ornaments -->
    <rect role="img" aria-label="Hop cone with leaves, line illustration" x="52" y="118" width="100" height="100" rx="40" fill="var(--hop-tone)" opacity="0.55"/>
    <rect role="img" aria-label="Hop cone with leaves, line illustration" x="456" y="118" width="100" height="100" rx="40" fill="var(--hop-tone)" opacity="0.55"/>

    <!-- medallion -->
    <circle class="rule" cx="304" cy="313" r="186" stroke-width="2"/>
    <circle cx="304" cy="313" r="154" fill="url(#medallion)" stroke="var(--ink)" stroke-width="2"/>
    <g role="img" aria-label="Portrait of the emperor in a light blue military tunic with medals" clip-path="url(#medallion-clip)">
      <rect x="150" y="160" width="310" height="310" fill="url(#portrait-tone)" opacity="0.75"/>
    </g>
    <text class="ring-title"><textPath href="#ring-arc" startOffset="50%" text-anchor="middle">CRAFT WEISSBIER</textPath></text>
    <g fill="var(--ink)">
      <circle cx="134" cy="276" r="2.2"/>
      <circle cx="131" cy="291" r="2.2"/>
      <circle cx="474" cy="276" r="2.2"/>
      <circle cx="477" cy="291" r="2.2"/>
    </g>

    <!-- hop wreath under portrait -->
    <path role="img" aria-label="Wreath of hop cones and leaves" d="M110,462 Q134,382 214,394 Q304,420 394,394 Q474,382 498,462 Z" fill="var(--hop-tone)" opacity="0.6"/>

    <!-- banner -->
    <path d="M92,470 L108,505 L92,548 L118,540 Z" fill="var(--ribbon)" stroke="var(--ink)" stroke-width="1.6"/>
    <path d="M516,470 L500,505 L516,548 L490,540 Z" fill="var(--ribbon)" stroke="var(--ink)" stroke-width="1.6"/>
    <path d="M100,462 Q304,446 508,462 L500,540 Q304,524 108,540 Z" fill="var(--ribbon)" stroke="var(--ink)" stroke-width="2"/>
    <text class="brand-mark" x="317" y="522" text-anchor="middle">RTB</text>
    <rect x="192" y="538" width="224" height="26" rx="13" fill="var(--ribbon-pill)" stroke="var(--ink)" stroke-width="1.2"/>
    <text class="origin" x="306" y="556" text-anchor="middle">LINDGRUBE.1853</text>

    <text class="full-name" x="304" y="610" text-anchor="middle">REINHOLD TOBIAS BAUMGART</text>

    <!-- specs -->
    <text class="specs" x="34" y="470">ALC. 5.1 %</text>
    <text class="specs" x="34" y="490">OG 12.6 °</text>
    <text class="specs" x="34" y="510">EBU 15</text>
    <text class="volume" x="578" y="486" text-anchor="end">0.5 L</text>
  </svg>
</div>
</body>
</html>
```